Recycling and Rubbish services for Residential and Commercial customers

We are after a complete redesign or freshening up of our current website.
www.tidlowe.co.nz
On this site the general public can rent or buy rollaTUBs or skips for rubbish and recycling collection around the Nelson and Tasman area of New Zealand.

Target Market(s)

18 to 100 year old males and females in Nelson and Tasman area of New Zealand

Industry/Entity Type

Waste Management

Contact Information for Business Card

logo name title email phone web site address all the normal stuff

Number of Pages Required

5+ page

Colors

Designer to choose colors to be used in the design.

Requirements
Must have
• Has to be very fast and easy for the customer to rent bin, skip, tags, liner etc..
• see web site www.tidlowe.co.nz
• An address finder so we can show two rates for urban and rural streets
Nice to have
• "We’re trying to get back to a more human face. Our customers appreciate that we are locals too. We are proud to be able to support our local community through sponsorship and donations."

```html
<!DOCTYPE html>
<html lang="en">
<head>
<meta charset="utf-8">
<title>Tid Lowe – Rubbish &amp; Recycling</title>
<link href="https://fonts.googleapis.com/css2?family=Rajdhani:wght@600;700&family=Roboto:wght@400;500;700&display=swap" rel="stylesheet">
<style>
:root{
  --green:#4a8a1c;
  --green-dark:#3b5f10;
  --green-deep:#2f4d0c;
  --red:#d62128;
  --orange:#f5a011;
  --ink:#1d1d1d;
  --grey-band:#e4e4e4;
  --footer:#262626;
  --footer-text:#c9c9c9;
  --white:#fff;
}
*{box-sizing:border-box;margin:0;padding:0}
html,body{width:1200px;height:2329px;overflow:hidden;background:var(--white);font-family:"Roboto",Arial,sans-serif;color:var(--ink)}
.page{position:relative;width:1200px;height:2329px;overflow:hidden}
.abs{position:absolute}

/* header */
.site-header{position:absolute;left:0;top:0;width:1200px;height:155px;background:linear-gradient(#fafafa,#e9e9e9)}
.brand{position:absolute;left:73px;top:23px;width:124px;height:109px;background:var(--green-dark);border:3px solid var(--white);box-shadow:0 0 0 1px #bbb;display:flex;align-items:center;justify-content:center;text-align:center;color:var(--white);font-family:"Rajdhani",sans-serif;font-weight:700;font-size:34px;line-height:34px}
.search{position:absolute;left:571px;top:23px;width:242px;height:39px;border:1px solid #bdbdbd;background:var(--white);font-size:14px;color:#666;padding:10px 12px}
.search svg{position:absolute;right:10px;top:9px}
.phone-icon{position:absolute;left:833px;top:17px;width:50px;height:50px;border-radius:50%;background:var(--red)}
.phone-icon svg{position:absolute;left:12px;top:12px}
.phone-label{position:absolute;left:892px;top:16px;font-family:"Rajdhani",sans-serif;font-weight:700;font-size:19px;color:var(--ink)}
.phone-number{position:absolute;left:892px;top:33px;font-family:"Rajdhani",sans-serif;font-weight:700;font-size:30px;color:var(--red)}
.main-nav{position:absolute;left:512px;top:106px;width:609px;height:46px;background:var(--green-dark);border-radius:8px 8px 0 0;display:flex;justify-content:center;align-items:center;gap:20px;color:var(--white);font-family:"Roboto",sans-serif;font-weight:500;font-size:16px}

/* hero */
.hero{position:absolute;left:0;top:155px;width:1200px;height:545px;background:linear-gradient(100deg,#5b8f3a 0%,#9eb4c9 25%,#3f68c0 45%,#c8ccd2 70%,#e9ecef 100%)}
.hero-curve{position:absolute;left:0;top:600px}
.finder-tab{position:absolute;left:450px;top:613px;width:308px;height:43px;background:var(--red);border-radius:10px 10px 0 0;color:var(--white);font-family:"Roboto",sans-serif;font-size:24px;text-align:center;line-height:45px}
.finder{position:absolute;left:151px;top:655px;width:897px;height:121px;background:var(--green);border:3px solid var(--green-deep);box-shadow:0 3px 6px rgba(0,0,0,.3);color:var(--white)}
.finder .hint{position:absolute;top:24px;font-size:12px}
.finder .field{position:absolute;top:43px;height:47px;background:var(--white);border:1px solid #aaa;color:#444;font-size:19px;padding:12px 16px}
.finder .go{position:absolute;left:645px;top:43px;width:66px;height:47px;background:var(--orange);color:var(--ink);font-weight:700;font-size:20px;text-align:center;line-height:47px;border:1px solid #d98a00}
.finder .zone{position:absolute;top:57px;font-size:17px;display:flex;align-items:center;gap:6px}
.finder .zone i{display:inline-block;width:13px;height:13px;border-radius:50%;background:var(--white);border:3px solid #ddd}
.finder .zone i.on{border-color:var(--white);background:var(--green-deep);box-shadow:0 0 0 2px var(--white)}

/* services band */
.service-band{position:absolute;left:0;top:975px;width:1200px;height:329px;background:linear-gradient(#4f8f1f,#437d17)}
.service-pill{position:absolute;top:823px;width:174px;height:321px;border-radius:87px;background:var(--green-dark);border:4px solid var(--white);box-shadow:0 4px 10px rgba(0,0,0,.35);color:var(--white);text-align:center}
.service-pill svg{position:absolute;left:37px;top:40px}
.service-pill .label{position:absolute;left:0;right:0;top:188px;font-family:"Rajdhani",sans-serif;font-weight:700;font-size:22px;line-height:22px}
.service-pill .plus{position:absolute;left:70px;top:250px;width:32px;height:32px;border-radius:50%;background:var(--white);color:var(--green-dark);font-weight:700;font-size:28px;line-height:31px}
.holiday{position:absolute;left:211px;top:1170px;width:778px;display:flex;align-items:center;gap:24px;color:var(--white);font-family:"Rajdhani",sans-serif;font-weight:700;font-size:24px;white-space:nowrap}
.holiday::before,.holiday::after{content:"";flex:1;height:1px;background:rgba(255,255,255,.6)}
.read-more{position:absolute;left:542px;top:1211px;width:115px;height:36px;background:var(--red);color:var(--white);font-size:14px;font-weight:500;text-align:center;line-height:36px}

/* products */
.section-title{position:absolute;left:0;width:1200px;text-align:center;font-family:"Rajdhani",sans-serif;font-weight:700;font-size:30px;color:var(--ink)}
.title-rule{position:absolute;left:562px;top:1389px;width:76px;height:3px;background:var(--green)}
.product-card{position:absolute;top:1424px;width:244px;height:265px;background:linear-gradient(#fff,#ececec);border:1px solid #dcdcdc;box-shadow:0 2px 4px rgba(0,0,0,.15)}
.product-card .photo{position:absolute;left:30px;top:22px;width:184px;height:150px;background:radial-gradient(ellipse at center,#6a8f4a 0%,#e8e8e8 70%)}
.product-card .cta{position:absolute;left:9px;top:212px;width:224px;height:43px;background:var(--red);color:var(--white);font-family:"Roboto",sans-serif;font-weight:500;font-size:17px;text-align:center;line-height:43px}

.quick-band{position:absolute;left:0;top:1746px;width:1200px;height:264px;background:var(--grey-band)}
.quick-title{position:absolute;left:355px;top:1796px;width:490px;display:flex;align-items:center;gap:30px;font-family:"Rajdhani",sans-serif;font-weight:700;font-size:30px;white-space:nowrap}
.quick-title::before,.quick-title::after{content:"";flex:1;height:1px;background:#aaa}
.quick-item{position:absolute;top:1855px;width:151px;height:98px;background:var(--white)}
.quick-item .photo{position:absolute;left:35px;top:12px;width:80px;height:74px}

/* footer */
.site-footer{position:absolute;left:0;top:2010px;width:1200px;height:319px;background:var(--footer);color:var(--footer-text)}
.footer-head{position:absolute;top:30px;font-size:22px;color:var(--white)}
.footer-small{position:absolute;font-size:15px;color:var(--footer-text)}
.footer-big{position:absolute;font-size:18px;color:var(--white)}
.newsletter{position:absolute;left:581px;top:77px;width:272px;height:39px;background:var(--white);color:#333;font-size:15px;padding:10px 10px}
.newsletter svg{position:absolute;right:10px;top:12px}
.social{position:absolute;left:907px;top:76px;display:flex;gap:6px}
.social span{width:37px;height:37px;border-radius:50%;border:2px solid #aaa;background:#3a3a3a}
.footer-rule{position:absolute;left:73px;top:264px;width:1054px;height:1px;background:#444}
</style>
</head>
<body>
<div class="page">

  <header class="site-header">
    <div class="brand">Tid<br>Lowe</div>
    <div class="search">Search
      <svg width="20" height="20" viewBox="0 0 20 20"><circle cx="8" cy="8" r="6" fill="none" stroke="#333" stroke-width="2"/><line x1="12.5" y1="12.5" x2="18" y2="18" stroke="#333" stroke-width="2"/></svg>
    </div>
    <div class="phone-icon">
      <svg width="26" height="26" viewBox="0 0 24 24"><path d="M6.6 10.8a15 15 0 0 0 6.6 6.6l2.2-2.2a1 1 0 0 1 1-.25 11.4 11.4 0 0 0 3.6.57 1 1 0 0 1 1 1V20a1 1 0 0 1-1 1A17 17 0 0 1 3 4a1 1 0 0 1 1-1h3.5a1 1 0 0 1 1 1c0 1.25.2 2.45.57 3.57a1 1 0 0 1-.25 1z" fill="#fff"/></svg>
    </div>
    <div class="phone-label">PHONE</div>
    <div class="phone-number">(03) 555 0199</div>
    <nav class="main-nav"><span>HOME</span><span>ABOUT US</span><span>SERVICES</span><span>TESTIMONIALS</span><span>FAQ</span><span>CONTACT US</span></nav>
  </header>

  <div class="hero" role="img" aria-label="Photo of a collection truck lifting a blue recycling bin on a suburban street"></div>
  <svg class="hero-curve" width="1200" height="110" viewBox="0 0 1200 110"><path d="M0 55 Q600 -40 1200 55 L1200 110 L0 110 Z" fill="#fff"/></svg>

  <div class="finder-tab">FIND A LOCATION</div>
  <div class="finder">
    <span class="hint" style="left:26px">Enter your street number.</span>
    <span class="hint" style="left:196px">Enter the first few letters of your street and select from the drop down box.</span>
    <div class="field" style="left:26px;width:159px">No</div>
    <div class="field" style="left:196px;width:438px">Your Street</div>
    <div class="go">Go</div>
    <div class="zone" style="left:729px"><i class="on"></i>Urban</div>
    <div class="zone" style="left:808px"><i></i>Rural</div>
  </div>

  <div class="service-band"></div>

  <div class="service-pill" style="left:214px">
    <svg width="100" height="120" viewBox="0 0 100 120" fill="none" stroke="#fff" stroke-width="3"><path d="M50 100 C30 75 18 60 18 42 a32 32 0 0 1 64 0 C82 60 70 75 50 100Z"/><path d="M41 35a9 9 0 1 1 13 8c-3 2-4 4-4 8"/><circle cx="50" cy="60" r="1.5" fill="#fff"/><line x1="8" y1="110" x2="30" y2="110" stroke-dasharray="3 5"/><line x1="70" y1="110" x2="92" y2="110" stroke-dasharray="3 5"/></svg>
    <div class="label">COLLECTION<br>AREA / DAYS</div><div class="plus">+</div>
  </div>
  <div class="service-pill" style="left:416px">
    <svg width="100" height="120" viewBox="0 0 100 120" fill="none" stroke="#fff" stroke-width="3"><rect x="10" y="25" width="80" height="45"/><rect x="18" y="33" width="64" height="29"/><circle cx="50" cy="47" r="14"/><text x="50" y="54" text-anchor="middle" fill="#fff" stroke="none" font-size="20" font-family="Roboto">$</text><path d="M30 70v40h40V85"/><path d="M30 85h20"/></svg>
    <div class="label">PAY<br>MY ACCOUNT</div><div class="plus">+</div>
  </div>
  <div class="service-pill" style="left:615px">
    <svg width="100" height="120" viewBox="0 0 100 120" fill="none" stroke="#fff" stroke-width="3"><path d="M38 12h24v8"/><rect x="18" y="20" width="64" height="10"/><path d="M22 30l6 80h44l6-80"/><circle cx="26" cy="105" r="8"/><path d="M40 50l-6-6m0 6v-6h6M60 50l6-6m0 6v-6h-6M40 72l-6 6m0-6v6h6M60 72l6 6m0-6v6h-6"/></svg>
    <div class="label">CHANGE<br>MY BIN SIZE</div><div class="plus">+</div>
  </div>
  <div class="service-pill" style="left:813px">
    <svg width="100" height="120" viewBox="0 0 100 120" fill="none" stroke="#fff" stroke-width="3"><path d="M5 62l20-18 20 18v22H5z"/><rect x="19" y="70" width="12" height="14"/><path d="M55 62l20-18 20 18v22H55z"/><rect x="69" y="70" width="12" height="14"/><path d="M25 38a30 30 0 0 1 50-6m0 0v-8m0 8h-8"/><path d="M75 94a30 30 0 0 1-50 6m0 0v8m0-8h8"/></svg>
    <div class="label">CHANGE<br>MY ADDRESS</div><div class="plus">+</div>
  </div>

  <div class="holiday">PUBLIC HOLIDAY COLLECTIONS</div>
  <div class="read-more">READ MORE</div>

  <h2 class="section-title" style="top:1351px">PRODUCT RANGE</h2>
  <div class="title-rule"></div>

  <div class="product-card" style="left:73px"><div class="photo" role="img" aria-label="Two green wheeled rubbish bins"></div><div class="cta">GET YOUR BIN HERE</div></div>
  <div class="product-card" style="left:343px"><div class="photo" role="img" aria-label="Green skip"></div><div class="cta">GET YOUR SKIP HERE</div></div>
  <div class="product-card" style="left:613px"><div class="photo" role="img" aria-label="Large green commercial bin with cardboard recycling cage"></div><div class="cta">GET COMMERCIAL BIN</div></div>
  <div class="product-card" style="left:883px"><div class="photo" role="img" aria-label="Bin supplies: liners, stickers and tags"></div><div class="cta">GET BIN SUPPLIES</div></div>

  <div class="quick-band"></div>
  <h2 class="quick-title">QUICK BUY SUPPLIES</h2>
  <div class="quick-item" style="left:183px"><div class="photo" role="img" aria-label="Roll of bin liners" style="background:linear-gradient(#e6ecd9,#c4d4a8)"></div></div>
  <div class="quick-item" style="left:354px"><div class="photo" role="img" aria-label="Pack of 120L liners" style="background:linear-gradient(#4d6338,#2f4222)"></div></div>
  <div class="quick-item" style="left:525px"><div class="photo" role="img" aria-label="Pack of 240L liners" style="background:linear-gradient(#4d6338,#2f4222)"></div></div>
  <div class="quick-item" style="left:695px"><div class="photo" role="img" aria-label="Blue bin tag" style="background:linear-gradient(#fff,#cfe4f7 50%,#fff)"></div></div>
  <div class="quick-item" style="left:866px"><div class="photo" role="img" aria-label="Red bin tag" style="background:linear-gradient(#fff,#f7cfcf 50%,#fff)"></div></div>

  <footer class="site-footer">
    <div class="footer-head" style="left:73px">Conatct Us</div>
    <svg class="abs" style="left:73px;top:76px" width="20" height="22" viewBox="0 0 20 22" fill="none" stroke="#bbb" stroke-width="1.5"><path d="M10 20C5 14 3 11 3 8a7 7 0 0 1 14 0c0 3-2 6-7 12z"/><circle cx="10" cy="8" r="2.5"/></svg>
    <div class="footer-small" style="left:107px;top:75px">Tid Lowe</div>
    <div class="footer-small" style="left:107px;top:97px">48 Harbour Ln, Nelson</div>
    <svg class="abs" style="left:73px;top:134px" width="20" height="20" viewBox="0 0 24 24" fill="none" stroke="#bbb" stroke-width="1.5"><path d="M6.6 10.8a15 15 0 0 0 6.6 6.6l2.2-2.2a1 1 0 0 1 1-.25 11.4 11.4 0 0 0 3.6.57 1 1 0 0 1 1 1V20a1 1 0 0 1-1 1A17 17 0 0 1 3 4a1 1 0 0 1 1-1h3.5a1 1 0 0 1 1 1c0 1.25.2 2.45.57 3.57a1 1 0 0 1-.25 1z"/></svg>
    <div class="footer-small" style="left:107px;top:133px">Call us</div>
    <div class="footer-big" style="left:107px;top:155px">(03) 555 0199</div>
    <svg class="abs" style="left:73px;top:198px" width="20" height="14" viewBox="0 0 20 14" fill="none" stroke="#bbb" stroke-width="1.5"><rect x="1" y="1" width="18" height="12"/><path d="M1 1l9 7 9-7"/></svg>
    <div class="footer-small" style="left:107px;top:195px">Email Us</div>
    <div class="footer-small" style="left:107px;top:218px">info@tidlowe.co.nz</div>

    <div class="footer-head" style="left:315px">Quick Links</div>
    <div class="footer-small" style="left:315px;top:75px">Home</div>
    <div class="footer-small" style="left:315px;top:103px">About Us</div>
    <div class="footer-small" style="left:315px;top:131px">Services</div>
    <div class="footer-small" style="left:315px;top:159px">Testimonials</div>
    <div class="footer-small" style="left:450px;top:75px">FAQ</div>
    <div class="footer-small" style="left:450px;top:103px">Media</div>
    <div class="footer-small" style="left:450px;top:131px">Links</div>
    <div class="footer-small" style="left:450px;top:159px">Contact Us</div>

    <div class="footer-head" style="left:581px">Subscribe Our Newsletter</div>
    <div class="newsletter">E-mail
      <svg width="36" height="14" viewBox="0 0 36 14" fill="none" stroke="#d62128" stroke-width="2"><path d="M0 7h34M27 1l7 6-7 6"/></svg>
    </div>

    <div class="footer-head" style="left:907px">Keep in Touch</div>
    <div class="social"><span></span><span></span><span></span><span></span></div>

    <div class="footer-rule"></div>
    <div class="footer-small" style="left:73px;top:283px;color:#fff;font-size:16px">Proud to be Nelson owned and operated!</div>
    <div class="footer-small" style="right:73px;top:285px;color:#ddd;font-size:14px">Copyright © 2017, Tid Lowe. All rights reserved.</div>
  </footer>

</div>
</body>
</html>
```